Pitch book for Birchmere Property Partners.

Birchmere Partners is a new real estate investment company focused on multifamily (apartment) investments along the San Francisco Peninsula (in other parts of the world it is also referred to as flats). We need a professional Pitch Book i.e. brochure (digital and print) to raise equity from private investors. Read about “pitch book” on Lexipedia. The profile of the investor is conservative and must qualify as an accredited investor. Think high net worth individuals, CEOs and wealthy retiring couples. The investor that is attracted to real estate invest because it is low risk, produce cash flow and provide solid returns over the long term.

The brochure should convey trust, be highly professional and be clean and crisp. I attach a PowerPoint doc to be used as a copy for the brochure. I also attach a brochure of Halvert Crane – I like the look and feel, think it was designed with InDesign.

We will use the brochure at one-on-one meetings with investors where we will present on a laptop; we also need it in a format so that we can email it, print it and use it to be uploaded as a website.

I prefer the up and down scroll format (like you would do on a Mac) compared to PowerPoint but I am open to suggestions.

The photos I used in the PowerPoint presentation was found on the web, please use your own stock images.

Target Market(s)

High net worth individuals

Industry/Entity Type

Real Estate

Font styles to use
Serif

Requirements
Must have
• See attached Power Point
Nice to have
• See attached HVC brochure, I like the look and feel.
Should not have
• I am open to your ideas.

```html
<!DOCTYPE html>
<html lang="en">
<head>
<meta charset="utf-8">
<title>Birchmere Partners — Pitch Book Spread</title>
<link href="https://fonts.googleapis.com/css2?family=Jost:wght@400;500;600&display=swap" rel="stylesheet">
<style>
  :root {
    --bg: #d9d9d9;
    --paper: #ffffff;
    --paper-shade: #ececec;
    --ink: #2b2b2b;
    --ink-soft: #444444;
    --frame: #5a5a5a;
    --tri-dark: #4a4a4a;
    --tri-light: #8a8a8a;
    --accent-red: #7a1418;
    --dusk-top: #3b2a6b;
    --dusk-mid: #5b4394;
    --dusk-low: #231a40;
  }
  * { box-sizing: border-box; margin: 0; padding: 0; }
  html, body { width: 1200px; height: 800px; overflow: hidden; }
  body {
    background: var(--bg);
    font-family: "Jost", "Futura", sans-serif;
    color: var(--ink);
    display: flex; align-items: center; justify-content: center;
  }
  .spread {
    width: 1120px; height: 700px;
    display: flex; position: relative;
    box-shadow: 0 6px 24px rgba(0,0,0,.25);
  }
  .page { width: 560px; height: 700px; position: relative; background: var(--paper); }
  .page--left { background: linear-gradient(90deg, var(--paper) 80%, var(--paper-shade)); }
  .page--right { background: linear-gradient(90deg, var(--paper-shade), var(--paper) 18%); }
  .hero {
    position: absolute; top: 32px; left: 0; width: 1120px; height: 200px; z-index: 2;
    background: linear-gradient(180deg, var(--dusk-top) 0%, var(--dusk-mid) 55%, var(--dusk-low) 100%);
  }
  .running-head { position: absolute; top: 7px; font-size: 12px; font-weight: 600; line-height: 1.1; z-index: 3; }
  .running-head small { display: block; font-size: 8px; font-weight: 500; }
  .page--left .running-head { left: 24px; }
  .page--right .running-head { right: 24px; text-align: right; }
  .page-title { font-size: 23px; font-weight: 400; margin-bottom: 18px; }
  .left-copy { position: absolute; top: 254px; left: 28px; width: 250px; }
  .point { font-size: 12.5px; line-height: 1.38; margin-bottom: 14px; color: var(--ink-soft); }
  .point b { font-weight: 600; color: var(--ink); }
  .map-frame {
    position: absolute; top: 256px; left: 296px; width: 236px; height: 320px;
    background: var(--frame); padding: 10px;
  }
  .map-area { width: 100%; height: 100%; background: linear-gradient(135deg, #e6e1d3 0%, #dfe8d5 45%, #b8d3ea 100%); }
  .folio { position: absolute; bottom: 14px; font-size: 12px; font-weight: 600; }
  .page--left .folio { left: 28px; }
  .page--right .folio { right: 24px; }
  .right-body { position: absolute; top: 248px; left: 36px; width: 480px; }
  .intro { font-size: 12.5px; line-height: 1.38; color: var(--ink-soft); margin-bottom: 16px; }
  .partner-row { display: flex; gap: 16px; align-items: flex-start; }
  .partner { font-size: 12px; line-height: 1.38; color: var(--ink-soft); margin-bottom: 12px; }
  .partner-name { display: flex; align-items: center; gap: 6px; font-size: 15px; font-weight: 600; color: var(--ink); margin-bottom: 4px; }
  .partner-name .mark { width: 14px; height: 14px; background: var(--ink); }
  .partner-name--red { color: var(--accent-red); font-size: 12.5px; }
  .partner-name--red .mark { background: var(--accent-red); width: 11px; height: 11px; }
  .partner-sub { display: block; font-size: 8.5px; font-weight: 500; color: var(--ink-soft); margin-top: -3px; margin-bottom: 4px; }
  .partner--narrow { width: 215px; }
  .team-diagram { width: 220px; height: 184px; flex: none; }
  .team-diagram text { font-family: "Jost", sans-serif; fill: #fff; text-anchor: middle; }
</style>
</head>
<body>
  <main class="spread">
    <div class="hero" role="img" aria-label="Photograph of a suspension bay bridge lit at dusk under a purple sky"></div>

    <section class="page page--left">
      <div class="running-head">San Francisco Peninsula<small>Multifamily Real Estate Investment</small></div>

      <div class="left-copy">
        <h2 class="page-title">Investment Protection</h2>
        <p class="point"><b>A world-class city</b> attracts entrepreneurs, innovators and industry which in turn creates high demand for housing.</p>
        <p class="point"><b>Supply constrained</b> markets, such as the San Francisco Peninsula, have strong investment fundamentals. This leads to higher occupancy, rental growth and preservation of capital.</p>
        <p class="point"><b>Laser-focus</b> on a small geographic market will result in superior investment outcomes.</p>
        <p class="point"><b>Multifamily properties</b> as an asset class has lower volatility, higher resilience during downturns and offers attractive risk-adjusted returns.</p>
        <p class="point"><b>Experienced management</b> team that can execute the investment strategy.</p>
      </div>

      <div class="map-frame">
        <div class="map-area" role="img" aria-label="Road map of the San Francisco Peninsula and Bay Area"></div>
      </div>

      <span class="folio">6</span>
    </section>

    <section class="page page--right">
      <div class="running-head">San Francisco Peninsula<small>Multifamily Real Estate Investment</small></div>

      <div class="right-body">
        <h2 class="page-title">Investment and Advisory Team</h2>
        <p class="intro">With 20 years of real estate investment and development experience, Birchmere Partners is ideally suited to execute the investment strategy.</p>

        <div class="partner-row">
          <div class="partner partner--narrow">
            <div class="partner-name"><span class="mark"></span>RAVELL DANE</div>
            <span class="partner-sub">REAL ESTATE SERVICES</span>
            The Ravell Dane Corporation has been providing property management services for over 49 years. They manage nearly 2,500 units with a combined value in excess of $500 million.
          </div>
          <svg class="team-diagram" viewBox="0 0 240 200" aria-label="Team structure diagram">
            <polygon points="120,0 240,200 0,200" fill="var(--tri-dark)"/>
            <polygon points="120,82 172,170 68,170" fill="var(--tri-light)"/>
            <text x="120" y="62" font-size="7.5">RAVELL DANE</text>
            <text x="120" y="71" font-size="6.5">Property Management</text>
            <text x="120" y="140" font-size="7.5">BIRCHMERE</text>
            <text x="120" y="149" font-size="6.5">Strategic Execution</text>
            <text x="54" y="184" font-size="6.5">HARTWELL, ASHBY</text>
            <text x="54" y="193" font-size="6.5">Legal and Financing</text>
            <text x="188" y="176" font-size="6.5">FERRIS &amp;</text>
            <text x="188" y="185" font-size="6.5">ASSOCIATES</text>
            <text x="188" y="194" font-size="6.5">Accounting</text>
          </svg>
        </div>

        <div class="partner">
          <div class="partner-name partner-name--red"><span class="mark"></span>HARTWELL ASHBY CORLAN &amp; REEVE LLP</div>
          Since 1929 their experienced attorneys provide effective drafting and negotiation services for real estate transactions throughout California.
        </div>

        <div class="partner">
          <div class="partner-name"><span class="mark"></span>FERRIS &amp; ASSOCIATES</div>
          <span class="partner-sub">Certified Public Accountants, Inc.</span>
          Based in Palo Alto, the Ferris &amp; Associates Public Accounting team has been delivering distinctive accounting services and have 100 years of combined experience.
        </div>
      </div>

      <span class="folio">7</span>
    </section>
  </main>
</body>
</html>
```